Holiday Rental Leaflet

Want a DL size double sided leaflet to distribute via local businesses, markets, family and friends
HOLIDAY RENTALCarrickalinga - 17 Farrow Street Sleeps 8-10 (2 Queen, 1 Double, 2 bunks), 4 bedrooms, BIR to all bedrooms 2 Bathrooms, one with bath, 2 toilets Open Plan Lounge/Dining/Kitchen area Dining Table for 8 peopleReverse cycle airconditionerSlow combustion wood heaterTV/DVD, CD/RadioKitchen has m/wave, oven, fridge/freezer, dishwasherBBQ providedTimber decking with 2 outside tables and 12 chairs Washing Machine and dryer provided One street back from beach Smoke free zone No Pets
For further information or to book contact Joan on 0491 278 306 or email joanbirch62@veltranet.com.au

Requirements
Nice to have
• Have sent a variety of photos of the house. No need to use all of them, pick out the most relevant for the leaflet.

```html
<!DOCTYPE html>
<html lang="en">
<head>
<meta charset="utf-8">
<title>Holiday Special Leaflet</title>
<link rel="stylesheet" href="https://fonts.googleapis.com/css2?family=Poppins:wght@300;700&family=Arimo:wght@700&display=swap">
<style>
  :root {
    --page-bg: #e6e6e4;
    --green: #1f9a3c;
    --green-dark: #137a2c;
    --green-light: #46b64e;
    --white: #ffffff;
    --orange: #f4a41c;
    --text-green: #12762b;
  }
  html, body {
    margin: 0;
    padding: 0;
    width: 977px;
    height: 1200px;
    overflow: hidden;
    background: var(--page-bg);
  }
  .leaflet {
    position: absolute;
    left: 20px;
    top: 335px;
    width: 937px;
    height: 530px;
    background: linear-gradient(160deg, var(--green-light) 0%, var(--green) 45%, var(--green-dark) 100%);
    overflow: hidden;
    font-family: "Poppins", sans-serif;
  }
  .leaflet-shapes {
    position: absolute;
    inset: 0;
  }
  .inset-photo {
    position: absolute;
    border: 6px solid var(--white);
    box-shadow: 0 3px 6px rgba(0,0,0,0.35);
  }
  .inset-photo--stove {
    left: 22px; top: 330px; width: 150px; height: 112px;
    transform: rotate(-6deg);
    background: linear-gradient(135deg, #c98a45, #8a5a2e 60%, #4d4038);
  }
  .inset-photo--dining {
    left: 200px; top: 312px; width: 150px; height: 118px;
    transform: rotate(3deg);
    background: linear-gradient(135deg, #e2a24e, #b8732f 55%, #8c5a2b);
  }
  .headline-box {
    position: absolute;
    left: 425px; top: 36px;
    width: 512px; height: 168px;
    background: rgba(120, 200, 120, 0.35);
    color: var(--white);
  }
  .headline-kicker {
    position: absolute;
    left: 22px; top: 14px;
    font-weight: 300;
    font-size: 21px;
    letter-spacing: 4px;
    margin: 0;
  }
  .headline-title {
    position: absolute;
    left: 20px; top: 44px;
    margin: 0;
    font-weight: 700;
    font-size: 58px;
    line-height: 58px;
    letter-spacing: -1px;
  }
  .feature-list {
    position: absolute;
    left: 425px; top: 214px;
    margin: 0; padding: 0;
    list-style: none;
    font-family: "Arimo", sans-serif;
    font-weight: 700;
    font-size: 12.5px;
    line-height: 15.2px;
    color: var(--white);
  }
  .feature-list li {
    position: relative;
    padding-left: 16px;
  }
  .feature-list li::before {
    content: "";
    position: absolute;
    left: 2px; top: 5px;
    width: 5px; height: 5px;
    background: var(--white);
  }
  .feature-list li.continued::before { display: none; }
  .contact-bar {
    position: absolute;
    left: 0; top: 465px;
    width: 100%; height: 42px;
    background: var(--orange);
    display: flex;
    align-items: center;
    padding-left: 22px;
    box-sizing: border-box;
    color: var(--text-green);
    white-space: nowrap;
  }
  .contact-lead { font-weight: 300; font-size: 20px; }
  .contact-name { font-weight: 700; font-size: 25px; margin-left: 8px; }
  .base-strip {
    position: absolute;
    left: 0; top: 507px;
    width: 100%; height: 23px;
    background: var(--green-dark);
  }
</style>
</head>
<body>
  <section class="leaflet">
    <svg class="leaflet-shapes" viewBox="0 0 937 530" width="937" height="530">
      <defs>
        <linearGradient id="house-tones" x1="0" y1="0" x2="0" y2="1">
          <stop offset="0" stop-color="#dfe6ec"/>
          <stop offset="0.35" stop-color="#9aa2a6"/>
          <stop offset="0.65" stop-color="#6e6a5e"/>
          <stop offset="1" stop-color="#8ea05a"/>
        </linearGradient>
      </defs>
      <path role="img" aria-label="Photo of the two-storey holiday house with timber deck and stairs"
            d="M0 0 H395 Q300 140 290 323 H0 Z" fill="url(#house-tones)"/>
      <path d="M395 0 Q300 140 290 323 Q275 410 205 465" fill="none" stroke="#ffffff" stroke-width="12"/>
      <path d="M418 0 Q322 140 312 323 Q298 410 232 465" fill="none" stroke="#7fcc7a" stroke-width="5" opacity="0.6"/>
    </svg>

    <div class="inset-photo inset-photo--stove" role="img" aria-label="Photo of the lounge with slow combustion wood heater"></div>
    <div class="inset-photo inset-photo--dining" role="img" aria-label="Photo of the timber dining area and kitchen"></div>

    <div class="headline-box">
      <p class="headline-kicker">Book right now your</p>
      <h1 class="headline-title">HOLIDAY<br>SPECIAL</h1>
    </div>

    <ul class="feature-list">
      <li>Sleeps 8-10</li>
      <li class="continued">(2 Queen, 1 Double, 2 bunks), 4 bedrooms,</li>
      <li class="continued">BIR to all bedrooms</li>
      <li>2 Bathrooms, one with bath, 2 toilets</li>
      <li>Open Plan Lounge/Dining/Kitchen area</li>
      <li>Dining Table for 8 people</li>
      <li>Reverse cycle air conditioner</li>
      <li>Slow combustion wood heater</li>
      <li>TV/DVD, CD/Radio</li>
      <li>Kitchen has m/wave, oven, fridge/freezer, dishwasher</li>
      <li>BBQ provided</li>
      <li>Timber decking with 2 outside tables and 12 chairs</li>
      <li>Washing Machine and dryer provided</li>
      <li>One street back from beach</li>
      <li>Smoke free zone</li>
      <li>No Pets</li>
    </ul>

    <div class="contact-bar">
      <span class="contact-lead">For further information or to book contact</span>
      <span class="contact-name">Joan on 0491 278 306</span>
    </div>
    <div class="base-strip"></div>
  </section>
</body>
</html>
```